FItness Bootcamp Flyer

We need an A4 flyer to distribute on an advertising board, and also distribute in the mail.

It should contain a photo(s) of females exercising and having fun outdoors.

It should contain the following text and if you think it could be worded better please change as I'm just looking at getting people to come along:

- KestrelMove Studio Outdoor Bootcamp
Get moving, get fit and feel great

Commencing 19th May

Get results before the winter season
6 Week Bootcamp for $49. Limited numbers!
Or casual visit $10 per session

Now is the time to:
- Lose Weight and Tone-up
- Build Strength and Endurance
- Increase Cardio Fitness
- Improve Your Energy and Vitality
- Fun Varied and Exciting Training Programs
- ALL Fitness Levels

LADIES ONLY BOOTCAMP SUBIACO
Monday 6:30-7:15am, 8:30-9:15am
Wednesday 6:30-7:!5am, 8:30-9:15am
Friday 8:30-9:15am,

Register you place now on 0428 574 812 or email: kestrelmovestudio@fernmail.net

facebook.com/KestrelMove Studio

Target Market(s)

Females 20-60yrs

Industry/Entity Type

Advertising

Requirements
Nice to have
• - We like the words and style of the Harbourline Open Air Training flyer attached
- Also the Vanta Group brochure
- I like the colour Blue, Green, Pink. They don't all have to be used but at least one would be nice thank you

```html
<!DOCTYPE html>
<html lang="en">
<head>
<meta charset="utf-8">
<title>KestrelMove Studio Outdoor Bootcamp</title>
<link rel="stylesheet" href="https://fonts.googleapis.com/css2?family=Baloo+2:wght@600;700;800&family=Overlock:ital,wght@1,700;1,900&family=Source+Sans+3:wght@600;700&family=Arimo:wght@400;700&display=swap">
<style>
  :root {
    --page: #ffffff;
    --band: #c994c6;
    --band-edge: #9c6c9e;
    --ink-dark: #151515;
    --ink-purple: #3a1f47;
    --ink-blue: #4652ad;
    --ink-navy: #262f7a;
    --shadow: #23285a;
    --teal: #82d1d3;
    --mint: #8fd8b8;
    --grass: #8fd46a;
    --frame: #80cfd0;
    --link: #4452b8;
  }
  * { margin: 0; padding: 0; box-sizing: border-box; }
  html, body { width: 1200px; height: 1000px; overflow: hidden; background: var(--page); }
  .flyer { position: absolute; left: 253px; top: 8px; width: 694px; height: 984px; overflow: hidden; font-family: "Baloo 2", sans-serif; }
  .photo { position: absolute; }
  .photo-weights { left: 0; top: 212px; width: 128px; height: 176px; background: linear-gradient(135deg, #d9e7c9, #e9a3a0 60%, #c9d6b7); }
  .photo-rest { left: 128px; top: 135px; width: 287px; height: 253px; background: linear-gradient(160deg, #e4e4e4, #b9b6a6 45%, #6f7a54); }
  .photo-run { left: 415px; top: 20px; width: 279px; height: 368px; background: linear-gradient(170deg, #5f8a3c, #8cba5c 50%, #5b7d3c); }
  .band { position: absolute; left: 0; top: 0; width: 694px; height: 240px; }
  .brand { position: absolute; left: 20px; top: 14px; font-weight: 800; font-size: 38px; line-height: 42px; color: var(--ink-dark); }
  .brand span { display: block; }
  .brand span:first-child { padding-left: 10px; }
  .tagline { position: absolute; left: 22px; top: 120px; font-weight: 700; font-size: 16px; color: var(--ink-purple); }
  .lower { position: absolute; left: 0; top: 388px; width: 694px; height: 596px; background: linear-gradient(180deg, var(--teal) 0%, var(--teal) 18%, var(--mint) 45%, var(--grass) 100%); }
  .headline { position: absolute; top: 26px; width: 100%; text-align: center; font-family: "Overlock", sans-serif; font-style: italic; font-weight: 900; font-size: 58px; line-height: 1; color: var(--ink-blue); text-shadow: 3px 3px 0 var(--shadow); }
  .offer { position: absolute; top: 94px; width: 100%; text-align: center; font-family: "Overlock", sans-serif; font-style: italic; font-weight: 900; font-size: 21px; line-height: 25px; color: var(--ink-blue); }
  .benefits { position: absolute; left: 27px; top: 183px; font-family: "Overlock", sans-serif; font-style: italic; font-weight: 900; font-size: 21px; line-height: 25px; color: var(--ink-navy); list-style: none; }
  .group-title { position: absolute; top: 352px; width: 100%; text-align: center; padding-left: 10px; font-family: "Source Sans 3", sans-serif; font-weight: 700; font-size: 27px; line-height: 36px; color: var(--ink-dark); }
  .schedule { position: absolute; left: 92px; top: 384px; width: 507px; height: 80px; background: #fff; border: 9px solid var(--frame); border-bottom: none; padding: 2px 0 0 115px; font-family: "Source Sans 3", sans-serif; font-weight: 700; font-size: 16px; line-height: 19px; color: var(--ink-dark); }
  .register { position: absolute; left: 40px; top: 459px; width: 628px; height: 110px; background: #fff; border: 9px solid var(--frame); padding-top: 0; text-align: center; font-family: "Arimo", sans-serif; font-size: 25px; line-height: 33px; color: var(--ink-dark); }
  .register b { font-weight: 700; }
  .register .social { color: var(--link); }
</style>
</head>
<body>
<main class="flyer">
  <div class="photo photo-weights" role="img" aria-label="Photo of women smiling while lifting light hand weights"></div>
  <div class="photo photo-rest" role="img" aria-label="Photo of a woman resting hands on knees after a run above a city view"></div>
  <div class="photo photo-run" role="img" aria-label="Photo of a woman jogging along a leafy forest trail"></div>

  <svg class="band" viewBox="0 0 694 240" aria-hidden="true">
    <path d="M0 0 H694 V32 C520 80 250 170 0 222 Z" fill="var(--band-edge)"/>
    <path d="M0 0 H694 V14 C520 62 250 152 0 206 Z" fill="var(--band)"/>
  </svg>
  <h1 class="brand"><span>KestrelMove Studio</span><span>Outdoor Bootcamp</span></h1>
  <p class="tagline">Get moving, get fit and feel great</p>

  <section class="lower">
    <h2 class="headline">Commencing 19th May</h2>
    <p class="offer">Get results before the winter season!<br>6 Week Bootcamp for $49 - Limited numbers!<br>Or casual visit $10 per session.</p>
    <ul class="benefits">
      <li>Now is the time to:</li>
      <li>- Lose Weight and Tone-up</li>
      <li>- Build Strength and Endurance</li>
      <li>- Increase Cardio Fitness</li>
      <li>- Improve Your Energy and Vitality</li>
      <li>- Complete Fun Varied and Exciting Training Programs</li>
    </ul>
    <h3 class="group-title">LADIES ONLY BOOTCAMP SUBIACO</h3>
    <div class="schedule">
      Monday .. 6:30-7:15am, 8:30-9:15am<br>
      Wednesday .. 6:30-7:15am, 8:30-9:15am<br>
      Friday .. 8:30-9:15am
    </div>
    <div class="register">
      Register you place now on: <b>0428 574 812</b><br>
      or email: <b>kestrelmovestudio@fernmail.net</b><br>
      <span class="social">www.fernsocial.net/KestrelMove Studio</span>
    </div>
  </section>
</main>
</body>
</html>
```